We need an attractive business card design that is modern and inviting. We like the blue and yellow (or gold) colors that are displayed with the logo. The business should communicate trust, experience, and integrity.

Target Market(s)

Residential and Commercial

Industry/Entity Type

Business

Contact Information for Business Card

Recessed Lighting
LED Retro Fit
Sign Repair
Alarms and Cameras
Mobile Home Services
24hr service calls

Font styles to use
Serif
Sans Serif

Colors
3176b5
0455a3
fece3e
fbee3e

Requirements
Must have
• Brondle Electric
• Owner: Marcus Tivane
• Licensed and Insured
• TECL #58917
Nice to have
• Exquisite Detail!!
• Over 20 years of experience
Should not have
• Nothing boring or traditional!!!

```html
<!DOCTYPE html>
<html lang="en">
<head>
<meta charset="utf-8">
<title>Brondle Electric – Business Card</title>
<link rel="stylesheet" href="https://fonts.googleapis.com/css2?family=Questrial&family=Montserrat:wght@500;700&display=swap">
<style>
  :root {
    --brand-blue: #0d55a3;
    --ink-blue: #0c4f9e;
    --brand-yellow: #ece62a;
    --card-white: #f4f4f4;
    --backdrop: #3b3b3b;
    --text-light: #ffffff;
  }
  html, body {
    margin: 0;
    padding: 0;
    width: 1200px;
    height: 965px;
    overflow: hidden;
    background: var(--backdrop);
  }
  .canvas {
    position: relative;
    width: 1200px;
    height: 965px;
  }
  .card {
    position: absolute;
    left: 246px;
    width: 710px;
    height: 404px;
    border-radius: 32px;
    overflow: hidden;
    background: radial-gradient(ellipse at 40% 40%, #ffffff 0%, var(--card-white) 60%, #e6e6e6 100%);
    box-shadow: 0 4px 10px rgba(0,0,0,0.45);
  }
  .card--front { top: 60px; }
  .card--back { top: 504px; }
  .card__art {
    position: absolute;
    inset: 0;
    width: 710px;
    height: 404px;
  }
  .brand {
    position: absolute;
    text-align: center;
  }
  .brand__mark {
    display: block;
    margin: 0 auto;
    border-radius: 50%;
    border-style: solid;
    border-color: var(--brand-blue);
    box-sizing: border-box;
  }
  .brand__name {
    display: block;
    font-family: "Montserrat", sans-serif;
    font-weight: 700;
    color: var(--ink-blue);
    white-space: nowrap;
    letter-spacing: 0.5px;
  }
  .card--front .brand { left: 40px; top: 150px; width: 280px; }
  .card--front .brand__mark { width: 66px; height: 66px; border-width: 5px; }
  .card--front .brand__name { font-size: 28px; margin-top: 6px; }

  .card--back .brand { left: 0; top: 50px; width: 710px; }
  .card--back .brand__mark { width: 92px; height: 92px; border-width: 6px; }
  .card--back .brand__name { font-size: 37px; margin-top: 4px; }

  .contact {
    position: absolute;
    left: 427px;
    top: 80px;
    font-family: "Questrial", sans-serif;
    color: var(--text-light);
  }
  .contact__name { margin: 0; font-size: 23px; font-weight: 400; line-height: 1.1; }
  .contact__role { margin: 0 0 20px; font-size: 16px; line-height: 1.2; }
  .contact__license { margin: 0 0 22px; font-size: 17px; line-height: 1.25; }
  .contact__lines { margin: 0 0 24px; padding: 0; list-style: none; font-size: 17px; line-height: 1.25; }
  .contact__lines li { display: flex; align-items: center; gap: 14px; }
  .contact__icon { width: 16px; height: 16px; flex: none; }
  .contact__company { margin: 0; font-size: 21px; line-height: 1.1; }
  .contact__city { margin: 0; font-size: 17px; line-height: 1.3; }

  .services {
    position: absolute;
    left: 0;
    top: 222px;
    width: 710px;
    margin: 0;
    text-align: center;
    font-family: "Montserrat", sans-serif;
    font-weight: 500;
    font-size: 16.5px;
    line-height: 30px;
    color: var(--ink-blue);
  }
  .tagline {
    position: absolute;
    left: 0;
    top: 375px;
    width: 710px;
    margin: 0;
    text-align: center;
    font-family: "Montserrat", sans-serif;
    font-weight: 500;
    font-size: 17px;
    color: var(--text-light);
  }
</style>
</head>
<body>
<main class="canvas">

  <section class="card card--front" aria-label="Business card front">
    <svg class="card__art" viewBox="0 0 710 404" aria-hidden="true">
      <path d="M284,0 Q434,202 276,404 L710,404 L710,0 Z" fill="var(--brand-blue)"/>
      <path d="M288,0 Q438,202 280,404 L710,404 L710,0 Z" fill="#ffffff"/>
      <path d="M292,0 Q446,202 284,404 L710,404 L710,0 Z" fill="var(--brand-yellow)"/>
      <path d="M322,0 Q458,202 316,404 L710,404 L710,0 Z" fill="var(--brand-blue)"/>
    </svg>

    <div class="brand">
      <span class="brand__mark"></span>
      <span class="brand__name">BRONDLE ELECTRIC</span>
    </div>

    <div class="contact">
      <h1 class="contact__name">Marcus Tivane</h1>
      <p class="contact__role">Owner</p>
      <p class="contact__license">Licensed and Insured<br>TECL #58917</p>
      <ul class="contact__lines">
        <li>
          <svg class="contact__icon" viewBox="0 0 16 16" aria-hidden="true"><path d="M3.5 1.5 L6 4 L4.8 6 C5.8 8 8 10.2 10 11.2 L12 10 L14.5 12.5 L12.5 14.5 C7 14 2 9 1.5 3.5 Z" fill="#fff"/></svg>
          <span>555-318-2607</span>
        </li>
        <li>
          <svg class="contact__icon" viewBox="0 0 16 16" aria-hidden="true"><rect x="1" y="3.5" width="14" height="9.5" fill="#fff"/><path d="M1.5 4 L8 9 L14.5 4" fill="none" stroke="var(--brand-blue)" stroke-width="1.3"/></svg>
          <span>info@brondleelectric.com</span>
        </li>
      </ul>
      <p class="contact__company">Brondle Electric :</p>
      <p class="contact__city">Harlow Creek,Texas</p>
    </div>
  </section>

  <section class="card card--back" aria-label="Business card back">
    <svg class="card__art" viewBox="0 0 710 404" aria-hidden="true">
      <path d="M0,272 Q355,424 710,280 L710,404 L0,404 Z" fill="var(--brand-blue)"/>
      <path d="M0,316 Q355,408 710,288 L710,404 L0,404 Z" fill="#ffffff"/>
      <path d="M0,320 Q355,404 710,292 L710,404 L0,404 Z" fill="var(--brand-yellow)"/>
      <path d="M0,330 Q355,414 710,322 L710,404 L0,404 Z" fill="var(--brand-blue)"/>
    </svg>

    <div class="brand">
      <span class="brand__mark"></span>
      <span class="brand__name">BRONDLE ELECTRIC</span>
    </div>

    <p class="services">
      Residential and Commercial, Recessed Lighting, LED Retro Fit<br>
      Sign Repair, Alarms and Cameras, Mobile Home Services, 24hr service calls
    </p>
    <p class="tagline">Exquisite Detail!! Over 20 years of experience</p>
  </section>

</main>
</body>
</html>
```